I need a design for my company's core values statement. This will be used on large posters (one as large as a wall), small posters, mouse pads, website, etc. I only need design, not content. The content should not change.

This is an IT company so it should be modern and impressive. Clean, sleek, professional are important guidelines. Our name is The Norvik Collective so space designs are not out of the question as long as they are not cliché or cheesey.

The values themselves should be the focus.

Here is the Core Values Statement as it is today:

THE NORVIK COLLECTIVE CORE VALUES

The Norvik Collective has resolved to make it clear to all stakeholders that we are a company which holds to certain core values and extolls the underlying virtues of that collective corporate conscience. Let it be known that following are the Core Values on which we base our personal behavior, our business dealings, and our daily decisions. Each member of the Norvik organization is held to these high standards on all levels of employment, interaction, and association.

THE NORVIK COLLECTIVE’S GUIDING PRINCIPLE:

“Treat everyone with the same high level of respect and care that customers receive.”
This principle applies to everyone we come in contact within the course of doing business while working for THE NORVIK COLLECTIVE. It pertains to clients of course, but also to colleagues, peers, subordinates, internal clients, vendors, and visitors.

OUR CORE VALUES

DELIVER EXCELLENCE
Exceed expectations.

BUILD TRUST
Through honesty, accountability, transparency, and accessibility.

BE A PEOPLE PERSON
Treat everyone with dignity and respect.

CREATE VALUE
Create and constantly deliver more value.
I
NNOVATE
Dream, innovate, create.

OWN IT
Take ownership.

Target Market(s)

International employees, clients, vendors

Industry/Entity Type

Business

Requirements
Must have
• Sleek, clean, modern, impressive. The values must be the focus
Nice to have
• We have a logo that I am attaching. it would be good to include, but not necessary.

```html
<!DOCTYPE html>
<html lang="en">
<head>
<meta charset="utf-8">
<title>The Norvik Collective Core Values</title>
<link rel="stylesheet" href="https://fonts.googleapis.com/css2?family=Source+Sans+3:wght@700&family=Open+Sans:wght@400&display=swap">
<style>
  :root {
    --page-bg: #ffffff;
    --sky-edge: #66c6f1;
    --sky-mid: #a6dcf6;
    --sky-glow: #e6f6fd;
    --ink-navy: #1e2a6f;
    --ink-body: #111111;
    --halo: #ffffff;
  }
  * { margin: 0; padding: 0; box-sizing: border-box; }
  html, body {
    width: 1200px;
    height: 1000px;
    overflow: hidden;
    background: var(--page-bg);
  }
  .canvas {
    position: relative;
    width: 1200px;
    height: 1000px;
  }
  .poster {
    position: absolute;
    left: 192px;
    top: 0;
    width: 816px;
    height: 1000px;
    overflow: hidden;
  }
  .poster-backdrop {
    position: absolute;
    inset: 0;
    background:
      radial-gradient(ellipse 60% 48% at 50% 46%, var(--sky-glow) 0%, var(--sky-mid) 55%, var(--sky-edge) 100%);
  }
  .poster-title {
    position: absolute;
    left: 0;
    right: 0;
    top: 104px;
    text-align: center;
    font-family: "Source Sans 3", sans-serif;
    font-weight: 700;
    font-size: 58px;
    line-height: 52px;
    color: var(--ink-navy);
    text-shadow: 0 0 6px var(--halo), 0 0 12px var(--halo);
  }
  .value {
    position: absolute;
    left: 0;
    right: 0;
    text-align: center;
  }
  .value-name {
    font-family: "Source Sans 3", sans-serif;
    font-weight: 700;
    font-size: 39px;
    line-height: 40px;
    color: var(--ink-navy);
    text-shadow: 0 0 5px var(--halo), 0 0 10px var(--halo);
  }
  .value-line {
    margin-top: 2px;
    font-family: "Open Sans", sans-serif;
    font-weight: 400;
    font-size: 20px;
    line-height: 29px;
    color: var(--ink-body);
    text-shadow: 0 0 4px var(--halo), 0 0 8px var(--halo);
  }
  .value--excellence { top: 254px; }
  .value--trust      { top: 362px; }
  .value--people     { top: 500px; }
  .value--create     { top: 609px; }
  .value--innovate   { top: 718px; }
  .value--own        { top: 827px; }
</style>
</head>
<body>
  <main class="canvas">
    <section class="poster">
      <div class="poster-backdrop" role="img" aria-label="Light blue sky backdrop with a soft white sunburst, faint concentric rings and twinkling stars"></div>

      <h1 class="poster-title">THE NORVIK COLLECTIVE<br>CORE VALUES</h1>

      <div class="value value--excellence">
        <h2 class="value-name">DELIVER EXCELLENCE</h2>
        <p class="value-line">Exceed expectations</p>
      </div>

      <div class="value value--trust">
        <h2 class="value-name">BUILD TRUST</h2>
        <p class="value-line">Through honesty, accountability, transparency,<br>and accessibility</p>
      </div>

      <div class="value value--people">
        <h2 class="value-name">BE A PEOPLE PERSON</h2>
        <p class="value-line">Treat everyone with dignity and respect</p>
      </div>

      <div class="value value--create">
        <h2 class="value-name">CREATE VALUE</h2>
        <p class="value-line">Create and constantly deliver more value</p>
      </div>

      <div class="value value--innovate">
        <h2 class="value-name">INNOVATE</h2>
        <p class="value-line">Dream, innovate, create</p>
      </div>

      <div class="value value--own">
        <h2 class="value-name">OWN IT</h2>
        <p class="value-line">Take ownership</p>
      </div>
    </section>
  </main>
</body>
</html>
```